依頼詳細
<現状サイトの課題>
①一目で、何をしている会社なのかが分からない。
⇒商品画像・作業画像などを入れ、分かりやすく目を引き付けるようにする。

②項目が小さく、引き付けにくいデザイン。
⇒アイコンを大きくして、デザイン性を持たせる。

③自社の強みを視覚化できていない。
⇒図や写真を追加し、視覚的に伝わるようにする。

④自社の新着情報がないので社内の動きが把握できない。
⇒新着ニュースを追加し社内の動きが把握できるようにする。

⑤企業規模が小さく感じてしまう。
⇒洗練されたデザイン、コンテンツの充実、グローバルサイトの作成により企業規模をワンランク大きく見えるように表現する。
----------------------------------
<現在のサイト>
明確なサイトの情報共有はできませんが、TOPページの情報を一部伏せて共有します。添付の”TOPページ”をご参照ください。

<サイトリニューアルの方針>
①強みを明確にする為、全体的に画像化し打ち出したい。TOPページは動画を掲載し、よりリアルにユーザー様にイメージが伝わるデザインにする。

②企業規模をワンランク大きく見えるように表現し、グローバル化についてもアピールすることで、事業規模の大きい信頼出来る会社であることが分かるようにし、新規顧客の獲得および定着するようにサイトリニューアルを行う。

③必須機能
・TOPページへ動画を埋め込む。
・スマホ対応(レスポンシブウェブデザイン)にする。
・ウェブ見積り機能を設け、いつでも見積りが確認できるようにする。(TOPページにバナーを設けるなどデザインする)

<イメージ参考サイト>
①メインカラーをブルーとし、TOPページを開くとすぐに大きな画像イメージが見えます。
https://www.e-hariwa.co.jp/

②トップページに表示される、動画イメージです。
https://www.dovel.co.jp/

③コンテンツの配置や施工事例が見やすいです。
http://www.tasemi-kk.com/

④TOPページに施工写真や文字が挿入されており分かりやすい。また企業イメージがよく考えられており、ブランディングされています。
http://www.fujiyaga.co.jp/

<カラーテーマ>
①青系(堅実・信頼・クール)または水色系(さわやか・清潔感)

②青4割、白6割の配色のイメージでお願いします。制作の際は、カラーチャート(カラーを選んだ理由)もご提示いただけると幸いです。

<重視する点/検討基準>
①サイトコンセプトにあったデザイン(ご提案の際は、制作頂いたデザインコンセプト及びデザイン説明コメントの記載をお願い致します)

②納期厳守

<具体的な制作数>
TOPページ:1ページ(PC版のデザイン制作をお願いします)

<選考の進め方>
ご提案頂いたデザイン内容・コンセプトなどをもとに、プロジェクトメンバーで選考、決定致します。
※今回は、トップページデザインのみの見積りとなります。
今後、コーディングを依頼する可能性もございます。その場合は改めてクリエタスを通じてご依頼させて頂きます。パララックスデザインでのコーディングも条件として入れてまいります。
1ページ
青系、水色系
• イラストレーター形式 (.ai)
• フォトショップ形式 (.psd)
追記です。
サイトコンセプトの資料も添付いたします。
宜しくお願いいたします。

クライアント様と協議させていただき、コンセプトに合った総合的なデザインを評価させて頂きました。
その中で、クライアント様からの評価が多かった「Pixfern様」を当選とさせていただきました。ありがとうございました。

ランサーの皆さん、このように沢山の素敵なデザインをご提案頂き本当にありがとうございました。
コンセプトを基に、クライアント様とも大いに悩んで決定させて頂きました。
また、選定が期限間近になってしまいましたこと、申し訳ございませんでした。

機会があれば、今後ともどうぞ宜しくお願い致します。

```html
<!DOCTYPE html>
<html lang="ja">
<head>
<meta charset="utf-8">
<title>御社 トップページ</title>
<link rel="stylesheet" href="https://fonts.googleapis.com/css2?family=Noto+Sans+JP:wght@400;500;700&family=Roboto:wght@400;500;700&display=swap">
<style>
:root{
  --blue:#0a68a6;
  --blue-dark:#084e80;
  --blue-light:#2d8fd0;
  --sky:#d6e8f4;
  --ink:#333;
  --muted:#666;
  --line:#d4d4d4;
  --panel:#f3f3f3;
  --accent:#e0572a;
  --footer:#1d2a36;
}
*{margin:0;padding:0;box-sizing:border-box}
html,body{width:1200px;height:4620px;overflow:hidden;background:#fff}
body{font-family:"Noto Sans JP",sans-serif;color:var(--ink);position:relative}
.abs{position:absolute}

/* header */
.header{left:0;top:0;width:1200px;height:120px}
.brand{left:24px;top:30px;font-size:34px;font-weight:700;color:#222}
.tagline{left:180px;top:44px;font-size:15px;color:var(--muted)}
.lang{right:20px;top:6px;font-size:13px;color:#fff;background:#555;padding:2px 10px}
.head-btn{top:44px;height:40px;width:150px;font-size:15px;color:#fff;display:flex;align-items:center;justify-content:center;gap:8px}
.head-btn.recruit{right:178px;background:var(--blue)}
.head-btn.contact{right:20px;background:var(--blue-dark)}

.nav{left:0;top:120px;width:1200px;height:112px;display:flex;border-top:1px solid var(--line);border-bottom:1px solid var(--line)}
.nav-item{flex:1;display:flex;flex-direction:column;align-items:center;justify-content:center;gap:8px;font-size:15px;color:#444;border-right:1px solid #e6e6e6}
.nav-item.active{background:var(--sky);color:var(--blue);border-bottom:4px solid var(--blue)}
.nav-item svg{width:44px;height:44px;stroke:var(--blue);fill:none;stroke-width:2.4}

/* hero */
.hero{left:0;top:232px;width:1200px;height:508px;background:linear-gradient(120deg,#bcd2e2 0%,#8fb4cf 45%,#5d89ad 100%)}
.hero-logo{left:460px;top:72px;width:280px;height:80px;border:3px solid #fff;background:rgba(10,60,100,.55);color:#fff;font-size:30px;font-weight:700;display:flex;align-items:center;justify-content:center}
.hero-copy{left:0;top:200px;width:1200px;text-align:center;color:#fff;font-size:21px;line-height:2.1}
.hero-copy span{background:rgba(10,45,80,.55);padding:2px 12px}
.hero-dots{left:520px;top:468px;display:flex;gap:10px}
.hero-dots i{display:block;width:30px;height:6px;background:rgba(255,255,255,.6)}
.hero-dots i.on{background:var(--blue)}

/* strengths */
.sec-title{width:1200px;left:0;text-align:center;font-size:36px;font-weight:700;color:#222}
.title-rule{left:330px;width:540px;height:10px;border-bottom:2px solid #333;border-radius:0 0 50% 50%}
.strengths{left:60px;top:920px;width:1080px;height:380px;display:flex}
.strength{flex:1;display:flex;flex-direction:column;align-items:center;border-right:2px solid var(--line)}
.strength:last-child{border-right:none}
.circle{width:250px;height:250px;border-radius:50%;background:radial-gradient(circle at 40% 30%,#3f9ede,#0a5c98 75%);display:flex;flex-direction:column;align-items:center;padding-top:40px;color:#fff}
.circle b{font-family:"Roboto",sans-serif;font-size:30px;font-weight:700}
.circle svg{margin-top:26px;width:100px;height:90px;stroke:#fff;stroke-width:3;fill:none}
.strength p{margin-top:28px;font-size:22px;text-align:center;line-height:1.6}
.strength em{font-style:normal;color:var(--blue);font-weight:700}
.strength em.accent{color:var(--accent)}

/* news */
.news-title{left:0;top:1370px;width:1200px;text-align:center;font-size:38px;font-weight:700;color:#222}
.news-title .i{color:var(--blue);font-style:italic;font-family:"Roboto",sans-serif;margin-right:8px}
.news-more{right:30px;top:1448px;font-size:17px;display:flex;align-items:center;gap:8px}
.news-more i{display:inline-block;width:22px;height:22px;background:#333;color:#fff;font-style:normal;font-size:14px;text-align:center;line-height:22px}
.news-list{left:30px;top:1490px;width:1140px;list-style:none;border-top:1px solid var(--line)}
.news-list li{height:52px;display:flex;align-items:center;font-size:20px;border-bottom:1px solid var(--line)}
.news-list time{width:190px;padding-left:2px}
.to-top{width:64px;height:64px;border-radius:50%;background:#222;display:flex;align-items:center;justify-content:center}

/* recruit */
.recruit-title{left:0;top:1730px;width:1200px;text-align:center;font-size:40px;font-weight:700;color:#222}
.sub-title{left:20px;font-size:36px;font-weight:700;color:#222;display:flex;align-items:center;gap:14px}
.sub-title::before{content:"";width:30px;height:30px;border-radius:50%;border:8px solid var(--blue);background:#fff}
.photo{background:linear-gradient(135deg,#dfe4ea,#9fb0c2)}
.program{left:20px;top:1960px;width:1160px;height:300px;display:flex}
.program .photo{width:400px;height:300px}
.program-text{flex:1;background:var(--blue);color:#fff;font-size:19px;line-height:2.3;padding:40px 0 0 60px}

.message{left:20px;width:1160px;height:410px;border:14px solid #dcdcdc;display:flex;background:#fff}
.message .body{flex:1;padding:26px 40px}
.message h4{font-size:20px;font-weight:500;padding-bottom:14px;border-bottom:2px solid var(--line);margin-bottom:26px}
.message p{font-size:18px;line-height:2.15}
.message .photo{width:370px}

/* table */
.req{left:20px;top:3360px;width:1160px;border-collapse:collapse;font-size:19px}
.req th{width:200px;background:var(--panel);font-weight:400;text-align:left;padding-left:22px;vertical-align:middle}
.req td{padding:14px 36px;line-height:1.85}
.req tr{border-bottom:1px solid var(--line)}
.req tr:first-child{border-top:1px solid var(--line)}

.process-lead{left:20px;top:4234px;font-size:20px}
.process{left:0;top:4320px;width:1200px;height:190px}
.footer{left:0;top:4580px;width:1200px;height:40px;background:var(--footer);color:#ccc;font-size:13px;text-align:center;line-height:40px}
</style>
</head>
<body>

<header class="header abs">
  <div class="brand abs">御社LOGO</div>
  <div class="tagline abs">クオリティーの高い鉄製品を短納期でご提供いたします。</div>
  <div class="lang abs">Japanese | Vietnamese</div>
  <a class="head-btn recruit abs">
    <svg width="16" height="16" viewBox="0 0 16 16"><rect x="1" y="4" width="14" height="10" fill="none" stroke="#fff" stroke-width="1.6"/><path d="M5 4V2h6v2" fill="none" stroke="#fff" stroke-width="1.6"/></svg>採用情報</a>
  <a class="head-btn contact abs">
    <svg width="16" height="16" viewBox="0 0 16 16"><rect x="1" y="3" width="14" height="10" fill="none" stroke="#fff" stroke-width="1.6"/><path d="M1 3l7 6 7-6" fill="none" stroke="#fff" stroke-width="1.6"/></svg>お問い合わせ</a>
</header>

<nav class="nav abs">
  <div class="nav-item active"><svg viewBox="0 0 44 44"><path d="M6 22L22 8l16 14"/><path d="M11 19v17h22V19"/></svg>トップページ</div>
  <div class="nav-item"><svg viewBox="0 0 44 44"><rect x="10" y="6" width="24" height="32"/><path d="M16 14h4M24 14h4M16 22h4M24 22h4M20 38v-7h4v7"/></svg>会社概要</div>
  <div class="nav-item"><svg viewBox="0 0 44 44"><rect x="6" y="14" width="32" height="22"/><path d="M16 14V8h12v6M6 24h32"/></svg>事業紹介</div>
  <div class="nav-item"><svg viewBox="0 0 44 44"><rect x="6" y="10" width="32" height="24"/><path d="M6 10l16 13 16-13"/></svg>お問い合せ</div>
  <div class="nav-item"><svg viewBox="0 0 44 44"><circle cx="22" cy="14" r="7"/><path d="M8 38c0-9 6-14 14-14s14 5 14 14"/></svg>採用情報</div>
  <div class="nav-item"><svg viewBox="0 0 44 44"><circle cx="14" cy="16" r="5"/><circle cx="30" cy="16" r="5"/><path d="M4 34c0-7 4-10 10-10s10 3 10 10M20 34c0-7 4-10 10-10s10 3 10 10"/></svg>スタッフ紹介</div>
  <div class="nav-item"><svg viewBox="0 0 44 44"><rect x="10" y="6" width="24" height="32"/><path d="M15 14h14M15 21h14M15 28h10"/></svg>社内報</div>
  <div class="nav-item"><svg viewBox="0 0 44 44"><path d="M8 30c0-8 6-14 14-14h14v14c0 4-3 6-6 6H14c-3 0-6-2-6-6z"/><path d="M16 26h14"/></svg>ブログ</div>
</nav>

<section class="hero abs" role="img" aria-label="鉄骨の螺旋階段とヘルメット姿の作業員の写真">
  <div class="hero-logo abs">御社のLOGO</div>
  <div class="hero-copy abs">
    <span>xxxxxxxxxxは四国を中心に建築階段、手摺などの</span><br>
    <span>鉄製品製造、鉄骨工事を行っております。</span><br>
    <span>お客様に良いサービスをご提供するため、培ってきた技術とネットワークを活かし</span><br>
    <span>最もご要望の多い「高品質・短納期」を実現いたしました。</span><br>
    <span>鉄製品の製造・工事のことなら短納期のxxxxxxxxxxにお任せください。</span>
  </div>
  <div class="hero-dots abs"><i class="on"></i><i></i><i></i><i></i></div>
</section>

<h2 class="sec-title abs" style="top:810px">私たちが選ばれる3つの強み</h2>
<div class="title-rule abs" style="top:862px"></div>

<div class="strengths abs">
  <div class="strength">
    <div class="circle"><b>Quality</b>
      <svg viewBox="0 0 100 90"><path d="M20 30l14-16h32l14 16-30 44z"/><path d="M20 30h60M40 14l-6 16 16 44 16-44-6-16"/></svg></div>
    <p><em class="accent">「高品質・短納期」</em><br>ご満足いただけるサービス</p>
  </div>
  <div class="strength">
    <div class="circle"><b>Consult</b>
      <svg viewBox="0 0 100 90"><circle cx="34" cy="30" r="12"/><circle cx="68" cy="30" r="12"/><path d="M12 78c0-16 10-26 22-26s22 10 22 26M46 78c0-16 10-26 22-26s22 10 22 26"/></svg></div>
    <p>なんでもご相談いただける<br><em>柔軟な体制</em></p>
  </div>
  <div class="strength">
    <div class="circle"><b>Professional</b>
      <svg viewBox="0 0 100 90"><path d="M14 70L8 24l26 22 16-30 16 30 26-22-6 46z"/><path d="M16 80h68"/></svg></div>
    <p><em>常にお客様目線</em>で<br>取り組み成長し続ける姿勢</p>
  </div>
</div>

<h2 class="news-title abs"><span class="i">i</span>新着情報</h2>
<a class="news-more abs"><i>›</i>お知らせ一覧を見る</a>
<ul class="news-list abs">
  <li><time>2016.12.20</time>年末年始のお知らせ</li>
  <li><time>2016.09.15</time>○○○の施工</li>
  <li><time>2016.08.01</time>ホームページリニューアルいたしました</li>
</ul>
<a class="to-top abs" style="left:1112px;top:1626px"><svg width="28" height="18" viewBox="0 0 28 18"><path d="M3 15L14 4l11 11" fill="none" stroke="#fff" stroke-width="4"/></svg></a>

<h2 class="recruit-title abs"><svg width="40" height="32" viewBox="0 0 40 32" style="vertical-align:-3px;margin-right:10px"><path d="M4 16L16 4l12 12-12 12z" fill="none" stroke="var(--blue-light)" stroke-width="4"/><path d="M16 16L28 4l8 8-12 12z" fill="var(--blue)"/></svg>採用情報</h2>

<h3 class="sub-title abs" style="top:1880px">人材育成プログラム</h3>
<div class="program abs">
  <div class="photo" role="img" aria-label="研修でプレゼンを受ける社員の写真"></div>
  <div class="program-text">
    人材育成プログラムについての説明がはいります。<br>
    人材育成プログラムについての説明がはいります。<br>
    人材育成プログラムについての説明がはいります。<br>
    人材育成プログラムについての説明がはいります。<br>
    人材育成プログラムについての説明がはいります。
  </div>
</div>

<h3 class="sub-title abs" style="top:2296px">先輩社員からのメッセージ</h3>
<article class="message abs" style="top:2390px">
  <div class="body">
    <h4>○○○○○事業部　○○○○○担当</h4>
    <p>先輩社員からのコメントがはいります。先輩社員からのコメ<br>ントがはいります。先輩社員からのコメントがはいります。<br>先輩社員からのコメントがはいります。<br>先輩社員からのコメントがはいります。先輩社員からのコメ<br>ントがはいります。先輩社員からのコメントがはいります。</p>
  </div>
  <div class="photo" role="img" aria-label="スーツ姿の男性社員の写真"></div>
</article>
<article class="message abs" style="top:2814px">
  <div class="photo" role="img" aria-label="白いブラウスの女性社員の写真"></div>
  <div class="body">
    <h4>○○○○○事業部　○○○○○担当</h4>
    <p>先輩社員からのコメントがはいります。先輩社員からのコメ<br>ントがはいります。先輩社員からのコメントがはいります。<br>先輩社員からのコメントがはいります。<br>先輩社員からのコメントがはいります。先輩社員からのコメ<br>ントがはいります。先輩社員からのコメントがはいります。</p>
  </div>
</article>

<a class="to-top abs" style="left:1112px;top:3264px"><svg width="28" height="18" viewBox="0 0 28 18"><path d="M3 15L14 4l11 11" fill="none" stroke="#fff" stroke-width="4"/></svg></a>
<h3 class="sub-title abs" style="top:3290px">募集要項</h3>
<table class="req abs">
  <tr style="height:66px"><th>雇用形態</th><td>正社員、契約社員</td></tr>
  <tr><th>勤務時間</th><td>フレックスタイム制（コアタイム10：00〜15：00）<br>※標準労働時間8時間／日</td></tr>
  <tr><th>給与</th><td>経験・能力を考慮の上、当社規定により決定します。<br>目標制度により、半年毎に人事考課を実施。<br>※月給も年2回見直します。</td></tr>
  <tr><th>待遇</th><td>昇給年2回（4月・10月）、賞与年2回（7月・12月）<br>交通費全額支給<br>各種社会保険完備（雇用・労災・健康・厚生年金）</td></tr>
  <tr><th>休日・休暇</th><td>完全週休2日制（土・日）、祝日<br>GW（暦どおり）、夏季、年末年始、有給（法定通り）、<br>慶弔、特別（長期休暇制度、誕生日休暇など）</td></tr>
</table>

<h3 class="sub-title abs" style="top:4170px">選考プロセス</h3>
<p class="process-lead abs">選考プロセスについての説明がここに入ります。</p>
<svg class="process abs" viewBox="0 0 1200 190" aria-label="選考の流れ">
  <rect x="0" y="0" width="1200" height="190" fill="#e8f1f8"/>
  <g font-family="Noto Sans JP, sans-serif" font-size="21" fill="#fff" text-anchor="middle">
    <polygon points="0,30 190,30 220,95 190,160 0,160" fill="#8cc3e6"/><text x="100" y="103">エントリー</text>
    <polygon points="200,30 390,30 420,95 390,160 200,160 230,95" fill="#6fb2df"/><text x="310" y="103">書類選考</text>
    <polygon points="400,30 590,30 620,95 590,160 400,160 430,95" fill="#4f9dd3"/><text x="510" y="103">一次面接</text>
    <polygon points="600,30 790,30 820,95 790,160 600,160 630,95" fill="#3489c4"/><text x="710" y="103">二次面接</text>
    <polygon points="800,30 990,30 1020,95 990,160 800,160 830,95" fill="#1d74b1"/><text x="910" y="103">最終面接</text>
    <polygon points="1000,30 1200,30 1200,160 1000,160 1030,95" fill="#0a5c98"/><text x="1110" y="103">内定</text>
  </g>
</svg>

<footer class="footer abs">Copyright© 2016 xxxxxxxxxxxx. All Rights Reserved.</footer>

</body>
</html>
```